We are needing a bookcover for a reprint of our book "Whispers Beneath the Amber Horizon". It takes a look at the geologic formation found in the great plains. Our original cover was colorful and showed rock layers. Something similar but different and eye catching would be great. a geologic cross section showing various layers or possibly some different rocks/soils. We are really open to suggestions attached is the current book cover with the colored layers and the cover from the 80s.

Target Market(s)

Adult Readers

Industry/Entity Type

Nonprofit retail - science - nature

Requirements
Must have
• Geology or rock layers
Nice to have
• Books title, Geologic cross section
Should not have
• People or animals, no photos prefer sketch

```html
<!DOCTYPE html>
<html lang="en">
<head>
<meta charset="UTF-8">
<title>Whispers Beneath the Amber Horizon — Book Cover</title>
<link href="https://fonts.googleapis.com/css2?family=Cinzel:wght@400;600;700&display=swap" rel="stylesheet">
<style>
  :root {
    --sky-teal: #8fc9b4;
    --cream: #f8f0d8;
    --sea-teal: #3c9ea6;
    --deep-navy: #0d2f3c;
    --sand-gold: #f2c56e;
    --rust-orange: #e2561b;
    --peach: #eaa466;
    --river-blue: #2896b4;
    --earth-brown: #3a1f12;
    --clay-grey: #8e8068;
    --ink: #111111;
    --paper: #ffffff;
  }
  html, body {
    margin: 0;
    padding: 0;
    width: 800px;
    height: 1200px;
    overflow: hidden;
    background: var(--cream);
  }
  .cover {
    position: relative;
    width: 800px;
    height: 1200px;
    overflow: hidden;
    font-family: "Cinzel", "Trajan Pro", serif;
  }
  .strata-art {
    position: absolute;
    inset: 0;
    background: linear-gradient(
      to bottom,
      var(--sky-teal) 0%,
      var(--sky-teal) 12%,
      var(--cream) 20%,
      var(--cream) 33%,
      var(--sea-teal) 40%,
      var(--deep-navy) 47%,
      var(--sand-gold) 54%,
      var(--rust-orange) 60%,
      var(--peach) 66%,
      var(--cream) 71%,
      var(--river-blue) 76%,
      var(--earth-brown) 83%,
      var(--clay-grey) 90%,
      var(--earth-brown) 100%
    );
  }
  .book-title {
    position: absolute;
    top: 42px;
    left: 0;
    width: 100%;
    margin: 0;
    text-align: center;
    color: var(--ink);
    font-weight: 700;
    line-height: 0.92;
  }
  .book-title span {
    display: block;
  }
  .title-large {
    font-size: 100px;
    letter-spacing: 0;
    margin-bottom: 2px;
  }
  .title-small {
    font-size: 52px;
    letter-spacing: 3px;
    margin: 8px 0 10px;
  }
  .series-label {
    position: absolute;
    bottom: 52px;
    left: 0;
    width: 100%;
    margin: 0;
    text-align: center;
    color: var(--paper);
    font-family: "Cinzel", serif;
    font-size: 27px;
    letter-spacing: 1.5px;
    font-weight: 600;
  }
</style>
</head>
<body>
  <main class="cover">
    <div class="strata-art" role="img" aria-label="Sketched geologic cross section of wavy rock layers in teal, navy, gold, orange, blue and brown beneath a pale sky"></div>
    <h1 class="book-title">
      <span class="title-large">WHISPERS</span>
      <span class="title-large">BENEATH</span>
      <span class="title-small">THE</span>
      <span class="title-large">AMBER</span>
      <span class="title-large">HORIZON</span>
    </h1>
    <p class="series-label">PRAIRIE EARTH SCIENCE SERIES</p>
  </main>
</body>
</html>
```